Velmar Ops Business Cards

We need to design some upbeat business cards. We are an Industrial Rope Access Company/Height Safety Company that specialize in Rope Access, Confined Space, Anchor Points, Safety Systems, PPE Inspecions and Rigging.
Company name is Velmar Ops Ltd
Card is for Gareth Lomas the Company Director
His mobile number is 027 418 9072 and email is gareth@velmarops.co.nz. Website address is www.velmarops.co.nz.
We will post some pictures below to ensure you get a good idea of what we do.

```html
<!DOCTYPE html>
<html lang="en">
<head>
<meta charset="utf-8">
<title>Velmar Ops – Business Cards</title>
<link href="https://fonts.googleapis.com/css2?family=Quicksand:wght@500;700&family=Roboto:wght@400&display=swap" rel="stylesheet">
<style>
  :root {
    --backdrop: #e6e4e0;
    --card-dark: #1c1e21;
    --card-light: #f2f2f2;
    --ink-light: #ffffff;
    --ink-dark: #1d1d1d;
    --ink-muted: #555555;
    --photo-deep: #15171a;
    --photo-mid: #4a4d52;
    --photo-glow: #c9c7c0;
  }
  * { margin: 0; padding: 0; box-sizing: border-box; }
  html, body { width: 1200px; height: 960px; overflow: hidden; }
  body { background: var(--backdrop); position: relative; font-family: "Quicksand", sans-serif; }

  .card {
    position: absolute;
    width: 600px;
    height: 343px;
    box-shadow: 0 3px 8px rgba(0,0,0,0.25);
    overflow: hidden;
  }
  .card--front { left: 314px; top: 113px; background: var(--card-dark); color: var(--ink-light); }
  .card--back  { left: 311px; top: 472px; background: var(--card-light); color: var(--ink-dark); }

  .front__photo {
    position: absolute;
    right: 0; top: 0;
    width: 330px; height: 100%;
    background:
      radial-gradient(circle at 62% 58%, var(--photo-glow) 0%, rgba(120,120,120,0.5) 12%, transparent 35%),
      radial-gradient(ellipse at 70% 30%, var(--photo-mid) 0%, transparent 60%),
      linear-gradient(90deg, var(--card-dark) 0%, var(--photo-deep) 25%, #2e3035 60%, #3a3c40 100%);
  }

  .front__brand {
    position: absolute; left: 55px; top: 56px;
    font-weight: 700; font-size: 29px; letter-spacing: 0.3px;
  }
  .front__marker {
    position: absolute; left: 0; top: 171px;
    width: 12px; height: 36px; background: var(--ink-light);
  }
  .front__name {
    position: absolute; left: 55px; top: 168px;
    font-weight: 700; font-size: 21px; text-transform: uppercase;
  }
  .front__role {
    position: absolute; left: 55px; top: 193px;
    font-weight: 700; font-size: 15px; text-transform: uppercase; letter-spacing: 0.3px;
  }
  .contact-list {
    position: absolute; left: 55px; top: 232px;
    list-style: none; font-weight: 500; font-size: 14px; text-transform: uppercase;
  }
  .contact-list li { display: flex; align-items: center; height: 19px; }
  .contact-list svg { width: 13px; height: 13px; margin-right: 9px; fill: var(--ink-light); }

  .back__brand {
    position: absolute; left: 0; right: 0; top: 122px;
    text-align: center; font-weight: 700; font-size: 50px; letter-spacing: 1px;
  }
  .services {
    position: absolute; left: 0; right: 0; top: 261px;
    text-align: center; font-family: "Roboto", sans-serif; font-size: 14.5px;
    color: var(--ink-muted); line-height: 19px;
  }
</style>
</head>
<body>
  <section class="card card--front">
    <div class="front__photo" role="img" aria-label="Photo of a rope access technician with a headlamp working inside a steel tank"></div>
    <div class="front__brand">Velmar Ops</div>
    <div class="front__marker"></div>
    <div class="front__name">Gareth Lomas</div>
    <div class="front__role">Company Director</div>
    <ul class="contact-list">
      <li>
        <svg viewBox="0 0 13 13"><path d="M3 0h7a1 1 0 0 1 1 1v11a1 1 0 0 1-1 1H3a1 1 0 0 1-1-1V1a1 1 0 0 1 1-1zm.6 1.5v8.5h5.8V1.5zM6.5 10.8a.8.8 0 1 0 0 1.6.8.8 0 0 0 0-1.6z"/></svg>
        027 418 9072
      </li>
      <li>
        <svg viewBox="0 0 13 13"><path d="M0 3h13v7H0zM0.8 3.6L6.5 7.6 12.2 3.6v-.1H.8z" fill-rule="evenodd"/></svg>
        gareth@velmarops.co.nz
      </li>
      <li>
        <svg viewBox="0 0 13 13"><circle cx="6.5" cy="6.5" r="6"/><path d="M3 3.5c1.5-.5 2.5.5 2 1.8-.6 1.4 1 1.8.6 3.2L4.2 10.6C3 9 2.4 6 3 3.5zM8 2c1.8.6 3 2.2 3 4-1 0-1.8-.8-2.6-.4C7.6 5 7.2 3.4 8 2z" fill="#1c1e21"/></svg>
        www.velmarops.co.nz
      </li>
    </ul>
  </section>

  <section class="card card--back">
    <div class="back__brand">Velmar Ops</div>
    <p class="services">
      Rope Access &bull; Anchor Points &bull; PPE Certification<br>
      Confined Space &bull; Safety Systems &bull; Rigging
    </p>
  </section>
</body>
</html>
```